Covid19 Poster for workplaces

Create a poster on how to protect yourself from Corona virus at work.
We are a Kindred Desk company. We have just re-branded so we need to fit in with our brand. We like clean and fresh, slightly amusing is ok if it will draw attention but it's an important topic. A4 and A3 please.

Content:

Headline: Lower the risk of COVID 19 in the workplace.

BE WELL

Bring your own cup - don’t share cups and food.
Elbow tap instead of handshakes and kisses
Wash your hands often - with soap.
Elbow or tissues when you cough or sneeze then straight in the bin
Leave your face alone after touching shared surfaces
Leave your bugs at home if you’re feeling unwell.

Call health line if you have a cough, a high temperature and shortness of breath. 0800 472 9160

Based on recommendations from ZPK and QLN

Target Market(s)

Employees - so anyone

Other font styles liked:
• Use the closest font to the brand documents

Requirements
Should not have
• Clip art

```html
<!DOCTYPE html>
<html lang="en">
<head>
<meta charset="utf-8">
<title>Be Well – Workplace Poster</title>
<link rel="stylesheet" href="https://fonts.googleapis.com/css2?family=Inter:wght@600;700;800&display=swap">
<style>
  :root {
    --teal: #1aa6b2;
    --teal-soft: #46b9c3;
    --white: #ffffff;
    --yellow: #f6d70c;
    --ink: #231f20;
  }
  html, body {
    margin: 0;
    padding: 0;
    overflow: hidden;
  }
  body {
    width: 849px;
    height: 1200px;
    font-family: "Inter", "Helvetica Neue", Arial, sans-serif;
  }
  .poster {
    position: relative;
    width: 849px;
    height: 1200px;
    background: var(--teal);
    color: var(--white);
    overflow: hidden;
  }
  .headline {
    position: absolute;
    left: 68px;
    top: 84px;
    margin: 0;
    font-size: 90px;
    line-height: 89px;
    font-weight: 700;
    letter-spacing: -3.5px;
  }
  .rule {
    position: absolute;
    height: 1px;
    background: var(--white);
  }
  .rule--top-left { left: 72px; width: 339px; top: 408px; }
  .rule--top-right { left: 437px; width: 339px; top: 408px; }
  .rule--mid-left { left: 72px; width: 339px; top: 539px; }
  .rule--mid-right { left: 437px; width: 339px; top: 539px; }
  .rule--footer { left: 72px; width: 704px; top: 1051px; }

  .motto {
    position: absolute;
    left: 68px;
    top: 424px;
    margin: 0;
    font-size: 84px;
    line-height: 100px;
    font-weight: 700;
    letter-spacing: -3px;
  }
  .tagline {
    position: absolute;
    left: 437px;
    top: 429px;
    margin: 0;
    font-size: 25px;
    line-height: 29.5px;
    font-weight: 700;
    letter-spacing: -0.5px;
  }

  .tip {
    position: absolute;
    display: flex;
    align-items: center;
  }
  .tip__icon {
    flex: none;
    border-radius: 12px;
    background: var(--teal-soft);
  }
  .tip__text {
    margin: 0;
    font-size: 19px;
    line-height: 22px;
    font-weight: 600;
    letter-spacing: -0.2px;
  }
  .tip--left { left: 73px; width: 360px; }
  .tip--left .tip__icon { width: 78px; height: 78px; margin-right: 13px; }
  .tip--right { left: 451px; width: 340px; }
  .tip--right .tip__icon { width: 70px; height: 70px; margin-right: 16px; }

  .tip--cup { top: 586px; }
  .tip--elbow { top: 698px; }
  .tip--wash { top: 811px; }
  .tip--sneeze { top: 590px; }
  .tip--face { top: 702px; }
  .tip--home { top: 815px; }

  .healthline {
    position: absolute;
    left: 72px;
    top: 958px;
    width: 720px;
    margin: 0;
    color: var(--yellow);
    font-size: 26.5px;
    line-height: 38px;
    font-weight: 700;
    letter-spacing: -0.6px;
  }
  .source {
    position: absolute;
    left: 72px;
    top: 1094px;
    margin: 0;
    font-size: 19px;
    line-height: 22px;
    font-weight: 700;
    letter-spacing: -0.3px;
  }
  .brand {
    position: absolute;
    right: 73px;
    top: 1090px;
    display: flex;
    align-items: center;
    gap: 12px;
  }
  .brand__dot {
    width: 44px;
    height: 44px;
    border-radius: 50%;
    background: var(--white);
  }
  .brand__name {
    margin: 0;
    color: var(--ink);
    font-size: 27px;
    line-height: 25px;
    font-weight: 800;
    letter-spacing: -0.8px;
  }
</style>
</head>
<body>
  <main class="poster">
    <h1 class="headline">Lower the risk of<br>COVID 19 in the<br>workplace!</h1>

    <div class="rule rule--top-left"></div>
    <div class="rule rule--top-right"></div>
    <p class="motto">BE WELL</p>
    <p class="tagline">People work better<br>when they feel good.<br>Simple.</p>
    <div class="rule rule--mid-left"></div>
    <div class="rule rule--mid-right"></div>

    <section class="tips">
      <div class="tip tip--left tip--cup">
        <div class="tip__icon" role="img" aria-label="Line icon of a steaming cup"></div>
        <p class="tip__text">Bring your own cup - don’t<br>share cups and food.</p>
      </div>
      <div class="tip tip--left tip--elbow">
        <div class="tip__icon" role="img" aria-label="Icon of a handshake crossed out"></div>
        <p class="tip__text">Elbow tap instead of<br>handshakes and kisses</p>
      </div>
      <div class="tip tip--left tip--wash">
        <div class="tip__icon" role="img" aria-label="Line icon of hands being washed with water drops"></div>
        <p class="tip__text">Wash your hands<br>often - with soap</p>
      </div>
      <div class="tip tip--right tip--sneeze">
        <div class="tip__icon" role="img" aria-label="Icon of a person sneezing into their elbow"></div>
        <p class="tip__text">Elbow or tissues when<br>you cough or sneeze then<br>straight in the bin</p>
      </div>
      <div class="tip tip--right tip--face">
        <div class="tip__icon" role="img" aria-label="Icon of a person touching their face"></div>
        <p class="tip__text">Leave your face alone<br>after touching shared<br>surfaces</p>
      </div>
      <div class="tip tip--right tip--home">
        <div class="tip__icon" role="img" aria-label="Icon of a head with a thermometer"></div>
        <p class="tip__text">Leave your bugs at home<br>if you’re feeling unwell</p>
      </div>
    </section>

    <p class="healthline">Call health line if you have a cough, a high temperature<br>and shortness of breath. 0800 472 9160</p>
    <div class="rule rule--footer"></div>

    <p class="source">Based on recommendations<br>from ZPK and QLN</p>
    <div class="brand">
      <span class="brand__dot"></span>
      <p class="brand__name">Kindred<br>Desk</p>
    </div>
  </main>
</body>
</html>
```